Manufacturers Catalog Cover Page

We are looking to have a cover to our catalog page designed. I currently have begun work for the remained of the catalog in InDesign and want the cover created in InDesign. I will provide photos.

Looking to beable to add the cover to our existing attached catalog.

Industry/Entity Type

Manufacturing

Requirements
Must have
• Colors match what we are currently using. The Dark grey and gold
Nice to have
• modern, clean

```html
<!DOCTYPE html>
<html lang="en">
<head>
<meta charset="utf-8">
<title>Meridian Polymers – Catalog Cover</title>
<link href="https://fonts.googleapis.com/css2?family=Montserrat:wght@300;400;500;700&display=swap" rel="stylesheet">
<style>
  :root {
    --page: #ffffff;
    --slate: #35332e;
    --slate-deep: #2b2a26;
    --gold: #d6b46a;
    --gold-soft: #b99a58;
    --ink-light: #f3f1ec;
    --rule: #5a5750;
  }
  * { box-sizing: border-box; margin: 0; padding: 0; }
  html, body {
    width: 1200px; height: 1200px; overflow: hidden;
    background: var(--page);
    font-family: "Montserrat", Arial, sans-serif;
  }
  .cover {
    position: absolute; left: 284px; top: 154px;
    width: 632px; height: 892px;
    background: radial-gradient(ellipse at 50% 40%, #3c3a35 0%, var(--slate) 55%, var(--slate-deep) 100%);
    color: var(--ink-light);
  }
  .brand {
    position: absolute; left: 146px; top: 34px;
    display: flex; align-items: center; gap: 14px;
  }
  .brand-mark {
    width: 72px; height: 72px; border-radius: 50%;
    background: var(--gold);
  }
  .brand-name {
    font-size: 18px; font-weight: 400; letter-spacing: 0.32em;
    line-height: 24px; color: var(--ink-light); text-transform: uppercase;
  }
  .wheel { position: absolute; left: 0; top: 0; }
  .headline {
    position: absolute; left: 0; width: 100%; top: 694px;
    text-align: center;
  }
  .headline-main {
    font-size: 33px; font-weight: 700; color: #ffffff; line-height: 40px;
  }
  .headline-sub {
    font-size: 34px; font-weight: 300; color: var(--gold); line-height: 42px;
    letter-spacing: 0.02em;
  }
  .divider {
    position: absolute; left: 108px; top: 796px; width: 416px; height: 1px;
    background: linear-gradient(90deg, transparent, var(--rule) 20%, var(--rule) 80%, transparent);
  }
  .contact {
    position: absolute; left: 0; width: 100%; top: 816px;
    display: flex; justify-content: center; gap: 20px;
    font-size: 15px; font-weight: 500; color: var(--ink-light);
  }
  .contact-item { display: flex; align-items: center; gap: 6px; }
  .contact-icon { width: 16px; height: 16px; }
  .website {
    position: absolute; left: 0; width: 100%; top: 845px;
    text-align: center; font-size: 14px; letter-spacing: 0.34em;
    color: var(--ink-light);
  }
  .website-name { color: var(--gold); }
</style>
</head>
<body>
<main class="cover">
  <header class="brand">
    <div class="brand-mark"></div>
    <div class="brand-name">Meridian<br>Polymers</div>
  </header>

  <svg class="wheel" width="632" height="700" viewBox="0 0 632 700">
    <defs>
      <linearGradient id="g-robots" x1="0" y1="0" x2="1" y2="1"><stop offset="0" stop-color="#9fb6cf"/><stop offset="1" stop-color="#d3b13a"/></linearGradient>
      <linearGradient id="g-building" x1="0" y1="0" x2="0" y2="1"><stop offset="0" stop-color="#8fb4dc"/><stop offset="1" stop-color="#e8ecef"/></linearGradient>
      <linearGradient id="g-boat" x1="0" y1="0" x2="1" y2="1"><stop offset="0" stop-color="#3d7fb8"/><stop offset="1" stop-color="#1f4f78"/></linearGradient>
      <linearGradient id="g-bus" x1="0" y1="0" x2="0" y2="1"><stop offset="0" stop-color="#5d7e55"/><stop offset="1" stop-color="#c9ced6"/></linearGradient>
      <linearGradient id="g-crane" x1="0" y1="0" x2="0" y2="1"><stop offset="0" stop-color="#f7f7f5"/><stop offset="1" stop-color="#c99a32"/></linearGradient>
      <linearGradient id="g-car" x1="0" y1="0" x2="0" y2="1"><stop offset="0" stop-color="#a9c6e0"/><stop offset="1" stop-color="#6d6c66"/></linearGradient>
      <linearGradient id="g-profiles" x1="0" y1="0" x2="1" y2="1"><stop offset="0" stop-color="#f3efea"/><stop offset="1" stop-color="#b5583a"/></linearGradient>
      <linearGradient id="g-strips" x1="0" y1="0" x2="1" y2="1"><stop offset="0" stop-color="#f6f2ee"/><stop offset="1" stop-color="#a8452c"/></linearGradient>
      <linearGradient id="g-refinery" x1="0" y1="0" x2="0" y2="1"><stop offset="0" stop-color="#6aa6d2"/><stop offset="0.45" stop-color="#cfe0e8"/><stop offset="0.55" stop-color="#b07a52"/><stop offset="1" stop-color="#9fc3d8"/></linearGradient>
    </defs>

    <circle cx="316" cy="404" r="253" fill="none" stroke="var(--gold-soft)" stroke-width="1.5"/>
    <circle cx="316" cy="404" r="248" fill="var(--slate-deep)"/>

    <g stroke="var(--slate-deep)" stroke-width="8" stroke-linejoin="round">
      <path role="img" aria-label="Industrial robot arms on a factory floor" fill="url(#g-robots)" d="M316 284 L316 156 A248 248 0 0 1 491.4 228.6 L400.85 319.15 A120 120 0 0 0 316 284 Z"/>
      <path role="img" aria-label="Modern office building with glass facade" fill="url(#g-building)" d="M400.85 319.15 L491.4 228.6 A248 248 0 0 1 564 404 L436 404 A120 120 0 0 0 400.85 319.15 Z"/>
      <path role="img" aria-label="Motor yacht cruising on open water" fill="url(#g-boat)" d="M436 404 L564 404 A248 248 0 0 1 491.4 579.4 L400.85 488.85 A120 120 0 0 0 436 404 Z"/>
      <path role="img" aria-label="City transit bus on a street" fill="url(#g-bus)" d="M400.85 488.85 L491.4 579.4 A248 248 0 0 1 316 652 L316 524 A120 120 0 0 0 400.85 488.85 Z"/>
      <path role="img" aria-label="Yellow mobile crane on a construction site" fill="url(#g-crane)" d="M316 524 L316 652 A248 248 0 0 1 140.6 579.4 L231.15 488.85 A120 120 0 0 0 316 524 Z"/>
      <path role="img" aria-label="Silver hatchback car on the road" fill="url(#g-car)" d="M231.15 488.85 L140.6 579.4 A248 248 0 0 1 68 404 L196 404 A120 120 0 0 0 231.15 488.85 Z"/>
      <path role="img" aria-label="Assorted rubber extrusion profiles" fill="url(#g-profiles)" d="M196 404 L68 404 A248 248 0 0 1 140.6 228.6 L231.15 319.15 A120 120 0 0 0 196 404 Z"/>
      <path role="img" aria-label="Coiled rubber sealing strips with adhesive backing" fill="url(#g-strips)" d="M231.15 319.15 L140.6 228.6 A248 248 0 0 1 316 156 L316 284 A120 120 0 0 0 231.15 319.15 Z"/>
    </g>

    <circle cx="316" cy="404" r="120" fill="var(--slate-deep)"/>
    <circle role="img" aria-label="Oil refinery reflected in calm water" cx="316" cy="404" r="110" fill="url(#g-refinery)"/>
    <circle cx="316" cy="404" r="106" fill="none" stroke="var(--gold)" stroke-width="1" opacity="0.7"/>
  </svg>

  <section class="headline">
    <h1 class="headline-main">Rubber &amp; Plastic Extursion</h1>
    <h2 class="headline-sub">GASKETS, TRIMS &amp; SEALS</h2>
  </section>

  <div class="divider"></div>

  <div class="contact">
    <span class="contact-item">
      <svg class="contact-icon" viewBox="0 0 16 16"><circle cx="8" cy="8" r="8" fill="var(--gold)"/><path d="M5.2 4.2l1.4-.3.8 1.9-.9.7c.4 1 1.1 1.7 2 2.1l.7-.9 1.9.8-.3 1.4c-3.2.2-5.8-2.5-5.6-5.7z" fill="var(--slate)"/></svg>
      888-555-0142
    </span>
    <span class="contact-item">
      <svg class="contact-icon" viewBox="0 0 16 16"><circle cx="8" cy="8" r="8" fill="var(--gold)"/><path d="M5.2 4.2l1.4-.3.8 1.9-.9.7c.4 1 1.1 1.7 2 2.1l.7-.9 1.9.8-.3 1.4c-3.2.2-5.8-2.5-5.6-5.7z" fill="var(--slate)"/></svg>
      330-555-0187
    </span>
  </div>

  <p class="website">www.<span class="website-name">meridianpolymers</span>.com</p>
</main>
</body>
</html>
```